Labeling for Organic Food

we need a label design for

1. Organic Red Rice
2. Organic wild honey

it is going to be the same design in different dimensions.

1. Organic Red Rice
Dimension 1 28*18.5cm
Dimension 2 13.5*8cm

2. Organic Honey
12*6cm
Updates

There is an update in the brief about using the Bhutanese color scheme. Please check it out.

Target Market(s)

people with the concern of health and the environment.

Requirements
Must have
• 1. our logo
• 2. All the info
• 3. A natural feel
• 4. I would prefer minimalistic style
• 5. Please include Bhutanese national colours as attached.

```html
<!DOCTYPE html>
<html lang="en">
<head>
<meta charset="utf-8">
<title>Organic Red Rice &amp; Wild Honey Labels</title>
<link href="https://fonts.googleapis.com/css2?family=Oswald:wght@500;600&family=Noto+Serif+SC:wght@400&display=swap" rel="stylesheet">
<style>
  :root {
    --bg: #f1f1f1;
    --black: #1e1e1e;
    --black-soft: #2a2a2a;
    --butter: #f6e18a;
    --gold: #e9cf5c;
    --gold-deep: #c9b04a;
    --rice-dark: #5e1a12;
    --rice-mid: #8f3222;
  }
  * { margin: 0; padding: 0; box-sizing: border-box; }
  html, body { width: 1200px; height: 898px; overflow: hidden; background: var(--bg); }
  .canvas { position: relative; width: 1200px; height: 898px; }

  /* Rice label */
  .rice-label {
    position: absolute; left: 258px; top: 198px; width: 368px; height: 528px;
    background: linear-gradient(180deg, var(--black) 0%, var(--black-soft) 30%, var(--black) 60%);
    overflow: hidden;
  }
  .rice-label__strip {
    position: absolute; left: 0; top: 0; width: 90px; height: 100%;
    background: var(--butter);
  }
  .rice-label__title {
    position: absolute; left: 45px; bottom: 20px;
    transform-origin: left bottom; transform: rotate(-90deg) translateY(0);
    white-space: nowrap;
    font-family: 'Oswald', sans-serif; font-weight: 600; font-size: 46px;
    color: var(--black); line-height: 1; letter-spacing: 0.5px;
  }
  .rice-label__origin {
    position: absolute; left: 82px; top: 228px;
    transform-origin: left bottom; transform: rotate(-90deg);
    white-space: nowrap;
    font-family: 'Oswald', sans-serif; font-weight: 500; font-size: 14px;
    color: var(--black); line-height: 1;
  }
  .rice-label__cn {
    position: absolute; left: 104px; top: 58px;
    font-family: 'Noto Serif SC', serif; font-size: 36px; color: var(--gold);
    letter-spacing: 1px;
  }
  .rice-label__window { position: absolute; left: 102px; top: 218px; }
  .rice-label__weight {
    position: absolute; right: 24px; bottom: 18px;
    font-family: 'Oswald', sans-serif; font-weight: 500; font-size: 19px; color: var(--gold);
  }

  /* Honey label */
  .honey-label { position: absolute; left: 760px; top: 462px; width: 240px; height: 220px; }
  .honey-label__shape { position: absolute; inset: 0; }
  .honey-label__text {
    position: absolute; inset: 0; display: flex; flex-direction: column; align-items: center;
    font-family: 'Oswald', sans-serif; font-weight: 500; color: var(--gold);
  }
  .brand-mark {
    margin-top: 30px; display: flex; align-items: center; gap: 6px;
    font-size: 15px; letter-spacing: 1px;
  }
  .brand-mark__dot { width: 8px; height: 8px; border-radius: 50%; background: var(--gold); }
  .honey-label__name { margin-top: 18px; font-size: 25px; font-weight: 600; line-height: 1; transform: scaleX(0.88); }
  .honey-label__cn { font-family: 'Noto Serif SC', serif; font-size: 19px; margin-top: 4px; letter-spacing: 1px; }
  .honey-label__origin { font-size: 15px; margin-top: 10px; }
  .honey-label__weight { font-size: 12px; margin-top: 18px; }
</style>
</head>
<body>
<main class="canvas">

  <section class="rice-label">
    <div class="rice-label__strip"></div>
    <h1 class="rice-label__title">ORGANIC RED RICE</h1>
    <p class="rice-label__origin">PRODUCT OF BHUTAN</p>
    <p class="rice-label__cn">有机红米</p>
    <svg class="rice-label__window" width="244" height="252" viewBox="0 0 244 252" role="img" aria-label="Photograph of red rice grains">
      <defs>
        <linearGradient id="riceTone" x1="0" y1="0" x2="1" y2="1">
          <stop offset="0" stop-color="var(--rice-mid)"/>
          <stop offset="1" stop-color="var(--rice-dark)"/>
        </linearGradient>
      </defs>
      <path d="M14 2 C90 22 180 90 238 222 Q242 248 220 248 L10 248 Q2 248 2 238 L2 14 Q2 -1 14 2 Z"
            fill="url(#riceTone)" stroke="var(--gold)" stroke-width="2.5"/>
    </svg>
    <p class="rice-label__weight">NET WEIGHT 500GM</p>
  </section>

  <section class="honey-label">
    <svg class="honey-label__shape" width="240" height="220" viewBox="0 0 240 220" aria-hidden="true">
      <rect x="0" y="38" width="240" height="144" fill="var(--gold-deep)" opacity="0.75"/>
      <rect x="206" y="38" width="34" height="144" fill="var(--butter)"/>
      <polygon points="62,0 178,0 238,110 178,220 62,220 2,110" fill="var(--black)"/>
    </svg>
    <div class="honey-label__text">
      <div class="brand-mark"><span class="brand-mark__dot"></span>DRUK MEADOW</div>
      <h2 class="honey-label__name">ORGANIC WILD HONEY</h2>
      <p class="honey-label__cn">有机野生蜂蜜</p>
      <p class="honey-label__origin">PRODUCT OF BHUTAN</p>
      <p class="honey-label__weight">NET WEIGHT 250ML</p>
    </div>
  </section>

</main>
</body>
</html>
```